Dornvale Trailers LLC

We need a flier designed to market our trailers. We would like to showcase some of the trailers we sell. Also we would like to target landscaping companies, construction companies, also for home use and recreational use.

```html
<!DOCTYPE html>
<html lang="en">
<head>
<meta charset="utf-8">
<title>Dornvale Trailers LLC – Flier</title>
<link href="https://fonts.googleapis.com/css2?family=Anton&family=Montserrat:wght@500;600;700;800&display=swap" rel="stylesheet">
<style>
  :root {
    --orange: #ee6a12;
    --ink: #141414;
    --paper: #f1f1ef;
    --paper-shade: #dcdcda;
    --backdrop: #e8e5e1;
    --text-grey: #3a3a3a;
    --photo-dark: #34373d;
    --photo-mid: #6e5c46;
    --photo-warm: #c27c3c;
  }
  * { box-sizing: border-box; margin: 0; padding: 0; }
  html, body { width: 1200px; height: 1200px; overflow: hidden; }
  body {
    background: var(--backdrop);
    font-family: "Montserrat", sans-serif;
    position: relative;
  }
  .flier {
    position: absolute;
    left: 160px; top: 35px;
    width: 880px; height: 1130px;
    background: var(--orange);
    overflow: hidden;
  }
  .flier__paper {
    position: absolute; inset: 0;
    background:
      radial-gradient(ellipse at 30% 20%, #fafafa 0%, transparent 55%),
      radial-gradient(ellipse at 75% 70%, #fbfbfb 0%, transparent 50%),
      radial-gradient(ellipse at 20% 85%, var(--paper-shade) 0%, transparent 45%),
      var(--paper);
    clip-path: polygon(0% 6%, 10% 4.5%, 22% 5%, 35% 3%, 50% 2%, 62% 1.5%, 74% 1%, 82% 0%, 84% 4%, 88% 8%, 93% 10%, 97% 12%, 100% 14%,
      100% 62%, 98% 64%, 99% 72%, 97% 78%, 98% 86%, 100% 90%, 100% 100%,
      8% 100%, 4% 96%, 0% 93%, 0% 6%);
  }
  .brand {
    position: absolute; top: 112px; left: 0; width: 100%;
    display: flex; justify-content: center; align-items: center; gap: 12px;
  }
  .brand__dot {
    width: 22px; height: 22px; border-radius: 50%;
    background: var(--orange);
  }
  .brand__name {
    font-weight: 800; font-size: 30px; letter-spacing: 1px;
    color: var(--orange); text-transform: uppercase;
  }
  .hero-photo {
    position: absolute; left: 0; top: 185px; width: 880px; height: 480px;
    background: radial-gradient(ellipse 60% 55% at 52% 55%, var(--photo-dark) 0%, var(--photo-mid) 55%, var(--photo-warm) 100%);
    clip-path: polygon(0% 12%, 8% 6%, 18% 9%, 28% 3%, 40% 7%, 52% 2%, 64% 6%, 76% 0%, 88% 5%, 100% 3%,
      100% 92%, 92% 96%, 80% 93%, 70% 98%, 58% 95%, 46% 100%, 34% 95%, 22% 98%, 10% 94%, 0% 97%);
  }
  .headline {
    position: absolute; left: 0; width: 100%; text-align: center;
    font-family: "Anton", sans-serif; text-transform: uppercase; line-height: 1;
  }
  .headline--premier { top: 598px; font-size: 106px; color: var(--orange); letter-spacing: 10px; padding-left: 10px; }
  .headline--destination { top: 700px; font-size: 118px; color: var(--ink); letter-spacing: 9px; padding-left: 9px; }
  .tagline {
    position: absolute; top: 818px; left: 0; width: 100%; text-align: center;
    font-weight: 700; font-size: 23px; color: var(--orange);
    letter-spacing: 0.8px; text-transform: uppercase;
  }
  .stripes {
    position: absolute; left: 8px; top: 735px; width: 18px; height: 165px;
    background: repeating-linear-gradient(135deg, #a9a9a9 0 4px, transparent 4px 9px);
  }
  .audiences {
    position: absolute; top: 890px; left: 134px; display: flex;
  }
  .audience {
    width: 160px; display: flex; flex-direction: column; align-items: center;
    border-right: 1px solid #b9b9b9; padding: 0 6px;
  }
  .audience:last-child { border-right: none; }
  .audience__icon {
    width: 72px; height: 72px; border-radius: 50%; background: var(--orange);
    display: flex; align-items: center; justify-content: center;
  }
  .audience__label {
    margin-top: 12px; font-weight: 700; font-size: 16px; line-height: 1.3;
    color: var(--ink); text-align: center;
  }
  .contact {
    position: absolute; top: 1058px; left: 0; width: 100%;
  }
  .contact__phone {
    position: absolute; left: 146px; top: 0;
    display: flex; align-items: center; gap: 8px;
    font-family: "Anton", sans-serif; font-size: 36px; color: var(--orange); letter-spacing: 1px;
  }
  .contact__block {
    position: absolute; top: 4px; font-size: 13.5px; font-weight: 500; color: var(--text-grey); line-height: 1.4;
  }
  .contact__block--address { left: 445px; }
  .contact__block--web { left: 670px; }
  .contact__row { display: flex; align-items: center; gap: 6px; }
  .contact__indent { padding-left: 16px; }
</style>
</head>
<body>
  <main class="flier">
    <div class="flier__paper"></div>

    <div class="brand">
      <span class="brand__dot"></span>
      <span class="brand__name">Dornvale Trailers</span>
    </div>

    <div class="hero-photo" role="img" aria-label="Product photo placeholder: black dump trailer with raised bed flanked by two open utility trailers with mesh ramps"></div>

    <h1 class="headline headline--premier">Premier</h1>
    <p class="headline headline--destination">Destination</p>
    <div class="stripes"></div>

    <p class="tagline">Top-quality trailers in Coleman, FL, and beyond!</p>

    <section class="audiences">
      <div class="audience">
        <div class="audience__icon">
          <svg width="42" height="42" viewBox="0 0 42 42" fill="#fff">
            <ellipse cx="14" cy="14" rx="7" ry="10"/><rect x="13" y="22" width="2" height="10"/>
            <ellipse cx="29" cy="18" rx="6" ry="9"/><rect x="28" y="25" width="2" height="8"/>
            <rect x="6" y="33" width="30" height="3" rx="1.5"/>
          </svg>
        </div>
        <p class="audience__label">landscaping<br>companies</p>
      </div>
      <div class="audience">
        <div class="audience__icon">
          <svg width="42" height="42" viewBox="0 0 42 42" fill="#fff">
            <rect x="18" y="20" width="16" height="10" rx="1"/>
            <polygon points="10,6 13,6 22,20 19,20"/>
            <rect x="8" y="6" width="2" height="10"/>
            <rect x="8" y="32" width="28" height="5" rx="2.5"/>
          </svg>
        </div>
        <p class="audience__label">Construction<br>companies</p>
      </div>
      <div class="audience">
        <div class="audience__icon">
          <svg width="42" height="42" viewBox="0 0 42 42" fill="#fff">
            <polygon points="21,6 4,21 9,21 9,36 18,36 18,27 24,27 24,36 33,36 33,21 38,21"/>
          </svg>
        </div>
        <p class="audience__label">Home<br>use</p>
      </div>
      <div class="audience">
        <div class="audience__icon">
          <svg width="42" height="42" viewBox="0 0 42 42" fill="#fff">
            <circle cx="11" cy="11" r="4"/>
            <circle cx="27" cy="16" r="9"/><rect x="26" y="24" width="2" height="12"/>
            <rect x="6" y="27" width="14" height="3"/><rect x="7" y="30" width="2" height="6"/><rect x="17" y="30" width="2" height="6"/>
          </svg>
        </div>
        <p class="audience__label">Recreational<br>use</p>
      </div>
    </section>

    <footer class="contact">
      <div class="contact__phone">
        <svg width="38" height="30" viewBox="0 0 38 30" fill="var(--orange)">
          <path d="M2 10 C8 2 30 2 36 10 L32 14 L27 10 L11 10 L6 14 Z"/>
          <rect x="8" y="14" width="22" height="14" rx="3"/>
        </svg>
        <span>(352) 555-0147</span>
      </div>
      <div class="contact__block contact__block--address">
        <div class="contact__row">
          <svg width="10" height="13" viewBox="0 0 10 13" fill="var(--orange)"><path d="M5 0a5 5 0 0 1 5 5c0 3-5 8-5 8S0 8 0 5a5 5 0 0 1 5-5z"/><circle cx="5" cy="5" r="2" fill="#fff"/></svg>
          <span>418 W Cedar Hollow Rd</span>
        </div>
        <div class="contact__indent">Coleman, FL 33521</div>
      </div>
      <div class="contact__block contact__block--web">
        <div class="contact__row">
          <svg width="12" height="12" viewBox="0 0 12 12"><circle cx="6" cy="6" r="6" fill="var(--orange)"/><path d="M0 6h12M6 0v12" stroke="#fff" stroke-width="1"/></svg>
          <span>dornvaletrailers.com</span>
        </div>
        <div class="contact__row">
          <svg width="12" height="10" viewBox="0 0 12 10"><rect width="12" height="10" rx="1" fill="var(--orange)"/><path d="M0 1l6 5 6-5" stroke="#fff" stroke-width="1.2" fill="none"/></svg>
          <span>sales@dornvaletrailers.com</span>
        </div>
      </div>
    </footer>
  </main>
</body>
</html>
```